5x8" package design for beauty / skin care product in a mylar bag

Brevona Works’ Glycolic Acid Powder is pure glycolic acid powder that, when mixed with water, creates glycolic acid solution. Depending on the amount of water added to the powder, you can create different strengths of the solution. Commerical products use between 10 and 70% glycolic acid solution in products. Brevona Works is part of the Calmora hair care company. One of our products use glycolic acid and we can repurpose the raw ingredient alone for retail sales targeting do-it-yourself at home beauty and skin care makers.

Most sellers of glycolic acid powder use basic packaging. Brevona Works intends to create professional, standout packaging that reinforces the quality of the glycolic acid powder we are selling and is consistent with other Calmora brand products sold.

Package design is for a 5x8" matte finished, top loading, resealable pouch. Just looking for front design initially. Second project will include back pouch design using format or design from the front of package.

```html
<!DOCTYPE html>
<html lang="en">
<head>
<meta charset="utf-8">
<title>Brevona Works Glycolic Acid Powder – Pouch Front</title>
<link rel="stylesheet" href="https://fonts.googleapis.com/css2?family=Jost:wght@400;500;700;800&display=swap">
<style>
  :root {
    --page-bg: #eef1f3;
    --pouch-blue: #6e96b2;
    --pouch-blue-light: #8cb1c6;
    --pouch-blue-dark: #5f88a4;
    --zip-band: #7fa6bd;
    --brand-ink: #2e4a45;
    --text-white: #ffffff;
    --badge-pink: #c17393;
    --structure-tint: rgba(255, 255, 255, 0.10);
    --powder-white: #f4f7f9;
    --powder-shadow: #b9c8d2;
  }
  * { box-sizing: border-box; margin: 0; padding: 0; }
  html, body {
    width: 1200px; height: 1200px; overflow: hidden;
    background: var(--page-bg);
    font-family: "Jost", sans-serif;
  }
  .canvas {
    position: relative; width: 1200px; height: 1200px;
    display: flex; align-items: center; justify-content: center;
  }
  .pouch {
    position: relative; width: 680px; height: 1088px;
    background: linear-gradient(180deg, var(--pouch-blue-light) 0%, var(--pouch-blue) 40%, var(--pouch-blue-dark) 100%);
    border-radius: 10px 10px 26px 26px;
    overflow: hidden;
    color: var(--text-white);
  }
  .zip-band {
    position: absolute; left: 0; right: 0; top: 70px; height: 30px;
    background: var(--zip-band);
    border-top: 1px solid rgba(255,255,255,0.25);
    border-bottom: 1px solid rgba(0,0,0,0.06);
  }
  .brand {
    position: absolute; top: 195px; left: 0; right: 0; text-align: center;
  }
  .brand-name {
    font-size: 56px; font-weight: 500; color: var(--brand-ink);
    letter-spacing: 1px; white-space: nowrap;
  }
  .product-title {
    position: absolute; top: 340px; left: 0; right: 0; text-align: center;
  }
  .product-title .line-bold {
    display: block; font-size: 60px; font-weight: 800; letter-spacing: 0.5px; line-height: 1.1;
  }
  .product-title .line-light {
    display: block; font-size: 56px; font-weight: 500; line-height: 1.2; margin-top: 6px;
  }
  .structure {
    position: absolute; background: var(--structure-tint); border-radius: 12px;
  }
  .structure-left { left: 40px; top: 500px; width: 150px; height: 200px; }
  .structure-right { left: 510px; top: 480px; width: 140px; height: 180px; }
  .structure-lower { left: 490px; top: 790px; width: 130px; height: 160px; }
  .powder-photo {
    position: absolute; left: 145px; top: 520px; width: 400px; height: 300px;
    border-radius: 48% 48% 44% 44% / 40% 40% 60% 60%;
    background: radial-gradient(ellipse at 50% 30%, var(--powder-white) 0%, #e2eaef 45%, var(--powder-shadow) 80%, #6f7c86 100%);
  }
  .free-from-badge {
    position: absolute; left: 0; top: 830px; width: 330px; height: 120px;
    background: var(--badge-pink);
    border-radius: 0 60px 60px 0;
    display: flex; align-items: center; gap: 14px; padding-left: 22px;
  }
  .free-from-badge .percent {
    font-size: 84px; font-weight: 500; line-height: 1;
  }
  .free-from-badge ul {
    list-style: none; font-size: 23px; font-weight: 500; line-height: 1.25; letter-spacing: 0.5px;
  }
  .uses {
    position: absolute; top: 972px; left: 0; right: 0; text-align: center;
    font-size: 21px; font-weight: 400;
  }
  .net-weight {
    position: absolute; top: 1025px; left: 0; right: 0; text-align: center;
    font-size: 20px; font-weight: 500; letter-spacing: 0.5px;
  }
</style>
</head>
<body>
<main class="canvas">
  <section class="pouch">
    <div class="zip-band"></div>

    <header class="brand">
      <span class="brand-name">Brevona Works</span>
    </header>

    <h1 class="product-title">
      <span class="line-bold">GLYCOLIC ACID</span>
      <span class="line-light">POWDER</span>
    </h1>

    <div class="structure structure-left" role="img" aria-label="Faint glycolic acid molecular structure diagram"></div>
    <div class="structure structure-right" role="img" aria-label="Faint glycolic acid molecular structure diagram"></div>
    <div class="structure structure-lower" role="img" aria-label="Faint glycolic acid molecular structure diagram"></div>

    <div class="powder-photo" role="img" aria-label="Photo of white glycolic acid powder heaped in a glass dish"></div>

    <div class="free-from-badge">
      <span class="percent">0%</span>
      <ul>
        <li>FRAGRANCES</li>
        <li>ADDITIVES</li>
        <li>DYES</li>
      </ul>
    </div>

    <p class="uses">Facial | Toner | Scalp Scrub | Hyperpigmentation</p>
    <p class="net-weight">NET WT. 100G</p>
  </section>
</main>
</body>
</html>
```